MS Word Template for Proposals and RFP

Looking for a nice looking graphic template in MS Word. We will use this to make proposals and answer RFPs. Looking for something that will match our company brand, but give a fresh, up-to-date look and feel. There are a few pictures of a template I like. I don't necessarily like that logo - looks too "kid like" for business, but I really like how clean and organized it is. Most proposals and RFP responses are looooooonnnngggg and boring - need something that someone can look through and find what they are looking for quickly and easily.
Updates

Can't wait to see your designs!

Target Market(s)

School districts and other governmental employers

Industry/Entity Type

Business

Requirements
Must have
• Must include sample table of contents, section dividers, charts, graphs and tables that we customized based on the content. The goal is for it to look simple, clean, compelling - organized so it's easy to read, easy to find your way around - good headers, charts, flow charts, tables.... etc. Looking to have 5-10 template pages that we can use to put together and entire portfolio.
Should not have
• No "cutsie" comic sans/apple for the teacher kind of stuff - we are selling employee benefits to schools and other governmental entities. Should be more serious and conservative but also look compelling and draw in the reader.

```html
<!DOCTYPE html>
<html lang="en">
<head>
<meta charset="utf-8">
<title>Table of Contents – Proposal Template</title>
<link href="https://fonts.googleapis.com/css2?family=Source+Sans+3:wght@400;600;700&display=swap" rel="stylesheet">
<style>
  :root {
    --canvas-bg: #ffffff;
    --page-shadow: rgba(0, 0, 0, 0.45);
    --brand-blue: #1f6fb7;
    --entry-grey: #3d3d3d;
    --wash-top: #ffffff;
    --wash-mid: #bcd6ec;
    --wash-bottom: #ffffff;
    --rule-light: rgba(255, 255, 255, 0.55);
    --footer-rule: #e6e9ee;
    --logo-grey: #9a9a9a;
  }

  * { margin: 0; padding: 0; box-sizing: border-box; }

  html, body {
    width: 927px;
    height: 1200px;
    overflow: hidden;
    background: var(--canvas-bg);
    font-family: "Source Sans 3", "Source Sans Pro", Arial, sans-serif;
  }

  .page {
    position: absolute;
    left: 33px;
    top: 31px;
    width: 862px;
    height: 1138px;
    background: linear-gradient(
      to bottom,
      var(--wash-top) 0%,
      #e4eef8 22%,
      var(--wash-mid) 46%,
      #e2edf7 72%,
      var(--wash-bottom) 91%,
      var(--wash-bottom) 100%
    );
    box-shadow: 0 0 6px 1px var(--page-shadow);
  }

  .page-title {
    position: absolute;
    left: 24px;
    top: 84px;
    font-size: 43px;
    font-weight: 700;
    letter-spacing: -0.2px;
    color: var(--brand-blue);
    line-height: 1;
  }

  .toc-divider {
    position: absolute;
    left: 434px;
    top: 262px;
    width: 1px;
    height: 596px;
    background: var(--rule-light);
  }

  .toc-list {
    position: absolute;
    left: 0;
    top: 334px;
    width: 100%;
    list-style: none;
  }

  .toc-entry {
    display: flex;
    height: 45.5px;
    font-size: 22px;
    font-weight: 600;
    line-height: 1;
  }

  .toc-section {
    width: 408px;
    text-align: right;
    color: var(--entry-grey);
  }

  .toc-pages {
    margin-left: 62px;
    color: var(--brand-blue);
  }

  .page-footer {
    position: absolute;
    left: 13px;
    right: 16px;
    top: 1054px;
    border-top: 1px solid var(--footer-rule);
    height: 84px;
    display: flex;
    justify-content: center;
    align-items: center;
    gap: 12px;
  }

  .footer-mark {
    width: 14px;
    height: 14px;
    background: var(--brand-blue);
  }

  .footer-name {
    font-size: 22px;
    font-weight: 600;
    letter-spacing: 2px;
    color: var(--brand-blue);
    text-transform: uppercase;
  }
</style>
</head>
<body>
  <main class="page">
    <h1 class="page-title">Table of Contents</h1>

    <div class="toc-divider"></div>

    <ol class="toc-list">
      <li class="toc-entry"><span class="toc-section">Lorem ipsum dolor sit</span><span class="toc-pages">Page 01 - 04</span></li>
      <li class="toc-entry"><span class="toc-section">Lorem ipsum</span><span class="toc-pages">Page 04 - 05</span></li>
      <li class="toc-entry"><span class="toc-section">Lorem ipsum dolor sit</span><span class="toc-pages">Page 06</span></li>
      <li class="toc-entry"><span class="toc-section">Lorem ipsum</span><span class="toc-pages">Page 07</span></li>
      <li class="toc-entry"><span class="toc-section">Lorem ipsum dolor sit</span><span class="toc-pages">Page 08 - 12</span></li>
      <li class="toc-entry"><span class="toc-section">Lorem ipsum</span><span class="toc-pages">Page 13 - 14</span></li>
      <li class="toc-entry"><span class="toc-section">Lorem ipsum dolor sit</span><span class="toc-pages">Page 15</span></li>
      <li class="toc-entry"><span class="toc-section">Lorem ipsum</span><span class="toc-pages">Page 16 - 20</span></li>
    </ol>

    <footer class="page-footer">
      <span class="footer-mark"></span>
      <span class="footer-name">Meridian Benefit Services</span>
    </footer>
  </main>
</body>
</html>
```